Business Card Design - PathwayMinds

Looking for creative, modern design, two sided for PathwayMinds that is consistent with color and feel of website www.pathwayminds.example.
Updates

Back of card will be used to promote products or have a quote revolving around decisions, change, leadership, innovation, creativity. Back should also have space to promote website, but optional to use the icon. Front of the card will need to use the icon and have standard place for name, job title, phone and email. We are not looking to put a mailing address or fax. Also want space to place a few words/phrase explaining what we do...such as individual growth and organizational development or tools, training, information...in addition, want the chatterbook icon small on the front somewhere as we are also on chatterbook.

Vector file uploaded of icon.

Target Market(s)

Professional coaching for individual growth and organizational development

Industry/Entity Type

Business

Requirements
Must have
• Icon...see attached.

```html
<!DOCTYPE html>
<html lang="en">
<head>
<meta charset="utf-8">
<title>PathwayMinds Business Card</title>
<link href="https://fonts.googleapis.com/css2?family=Lato:wght@400;700&display=swap" rel="stylesheet">
<style>
  :root {
    --page-bg: #e4e8ea;
    --card-bg: #ffffff;
    --brand-blue: #2a6fc0;
    --brand-blue-dark: #1f5aa3;
    --ink: #2b2b2b;
    --mark-light: #dfe8f4;
    --mark-mid: #9fb8d8;
    --white: #ffffff;
  }
  * { margin: 0; padding: 0; box-sizing: border-box; }
  html, body {
    width: 1200px; height: 960px; overflow: hidden;
    background: var(--page-bg);
    font-family: "Lato", sans-serif;
  }
  .sheet {
    width: 1200px; height: 960px;
    display: flex; flex-direction: column; align-items: center; justify-content: center;
    gap: 60px;
  }
  .card {
    position: relative;
    width: 700px; height: 400px;
    background: var(--card-bg);
    overflow: hidden;
    box-shadow: 0 6px 18px rgba(0,0,0,0.15);
  }

  /* Front */
  .holder-name {
    position: absolute; left: 36px; top: 112px;
    font-size: 32px; font-weight: 400; letter-spacing: 0.5px;
    color: var(--brand-blue); text-transform: uppercase;
  }
  .holder-title {
    position: absolute; left: 38px; top: 160px;
    font-size: 22px; color: var(--ink);
  }
  .contact-list {
    position: absolute; left: 38px; top: 226px;
    list-style: none;
  }
  .contact-list li {
    display: flex; align-items: center; gap: 12px;
    font-size: 21px; color: var(--ink);
    height: 32px;
  }
  .contact-icon { width: 20px; height: 20px; flex: none; }
  .social-square {
    width: 19px; height: 19px; background: var(--brand-blue); flex: none; border-radius: 2px;
  }
  .brand-block {
    position: absolute; right: 56px; top: 70px; width: 200px;
    display: flex; flex-direction: column; align-items: center; gap: 22px;
  }
  .brand-dot {
    width: 130px; height: 130px; border-radius: 50%;
    background: radial-gradient(circle at 45% 40%, var(--mark-light), var(--mark-mid));
    border: 8px solid var(--brand-blue);
  }
  .brand-name {
    font-size: 26px; font-weight: 400; color: var(--ink);
  }
  .tagline-band {
    position: absolute; left: 0; right: 0; top: 320px; height: 42px;
    background: var(--brand-blue);
    display: flex; align-items: center; justify-content: center;
    color: var(--white); font-size: 21px; letter-spacing: 0.3px;
  }

  /* Back */
  .back-mark {
    position: absolute; left: -110px; top: 40px;
    width: 300px; height: 300px; border-radius: 50%;
    background: radial-gradient(circle at 60% 45%, var(--mark-light), var(--mark-mid));
    border: 14px solid var(--brand-blue);
  }
  .back-brand-name {
    position: absolute; left: 230px; top: 150px;
    font-size: 34px; color: var(--brand-blue);
  }
  .web-band {
    position: absolute; left: 180px; right: 0; top: 292px; height: 34px;
    background: var(--brand-blue);
    display: flex; align-items: center; justify-content: flex-end;
    padding-right: 40px;
    color: var(--white); font-size: 18px; font-weight: 700; letter-spacing: 0.5px;
  }
</style>
</head>
<body>
<main class="sheet">
  <section class="card card-front" aria-label="Card front">
    <h1 class="holder-name">Marla Whitcombe</h1>
    <p class="holder-title">Chief Innovator</p>
    <ul class="contact-list">
      <li>
        <svg class="contact-icon" viewBox="0 0 20 20" aria-hidden="true">
          <rect x="1" y="1" width="18" height="18" rx="2" fill="none" stroke="#2a6fc0" stroke-width="2"/>
          <rect x="4" y="4" width="4" height="12" fill="#2a6fc0"/>
          <rect x="10" y="4" width="6" height="4" fill="#2a6fc0"/>
          <rect x="10" y="10" width="2" height="2" fill="#2a6fc0"/>
          <rect x="14" y="10" width="2" height="2" fill="#2a6fc0"/>
          <rect x="10" y="14" width="2" height="2" fill="#2a6fc0"/>
          <rect x="14" y="14" width="2" height="2" fill="#2a6fc0"/>
        </svg>
        1-800-555-0147
      </li>
      <li>
        <svg class="contact-icon" viewBox="0 0 20 20" aria-hidden="true">
          <rect x="1" y="4" width="18" height="12" fill="none" stroke="#2a6fc0" stroke-width="1.8"/>
          <polyline points="1,4 10,11 19,4" fill="none" stroke="#2a6fc0" stroke-width="1.8"/>
        </svg>
        contact@pathwayminds.example
      </li>
      <li>
        <span class="social-square" aria-hidden="true"></span>
        /pathwayminds
      </li>
    </ul>
    <div class="brand-block">
      <div class="brand-dot" aria-hidden="true"></div>
      <p class="brand-name">PathwayMinds</p>
    </div>
    <div class="tagline-band">individual growth and organizational development</div>
  </section>

  <section class="card card-back" aria-label="Card back">
    <div class="back-mark" aria-hidden="true"></div>
    <p class="back-brand-name">PathwayMinds</p>
    <div class="web-band">www.pathwayminds.example</div>
  </section>
</main>
</body>
</html>
```